BRQL project
Cloudward Trainer Bench Systems
i dont see, button or anything ,,,...
about handover...anyone help me..??
i am first in here..how way the rule and upload my file to ch....
The project has been extended for 3 more days.
Ruth.
Hi,
I want only static
hello ! my name is Ida :) I want to participate this nice contest ~! Haven't one .ai format logo ? I not understand static or animated banner !? please more details - thanks
or not of*
flash of animated gif?
I would like to see it animated also
Do you need it animated?
I would like to see also a new with the wgt lifter text to be replaced by Vortek WGT PC.
Also add the bellow text
Increase WGT performance by 30% and more
It would be great if you could give specific text content / copy. Please mention your preferred colors and other specifications(if any). A more detailed design brief would help.

```html
<!DOCTYPE html>
<html lang="en">
<head>
<meta charset="utf-8">
<title>Vortek WGT PC – Banner Set</title>
<link href="https://fonts.googleapis.com/css2?family=Fira+Sans+Extra+Condensed:wght@600;700&display=swap" rel="stylesheet">
<style>
  :root {
    --stage: #000000;
    --sky-top: #4f86c9;
    --sky-mid: #9cc0e4;
    --sky-low: #dfe9f2;
    --blue-light: #2266d0;
    --blue-deep: #0a1f86;
    --orange: #f7a21b;
    --white: #ffffff;
    --badge-ring: #1d4fa8;
  }
  * { margin: 0; padding: 0; box-sizing: border-box; }
  html, body { width: 1200px; height: 845px; overflow: hidden; background: var(--stage); }
  body { font-family: "Fira Sans Extra Condensed", "Arial Narrow", sans-serif; position: relative; }

  .banner { position: absolute; overflow: hidden; background: linear-gradient(180deg, var(--blue-light), var(--blue-deep)); color: var(--white); }
  .banner .photo { position: absolute; left: 0; top: 0; background: linear-gradient(180deg, var(--sky-top) 0%, var(--sky-mid) 55%, var(--sky-low) 100%); }
  .banner .swoosh { position: absolute; left: 0; top: 0; width: 100%; height: 100%; }

  .badge { position: absolute; border-radius: 50%; background: var(--white); border: 3px solid var(--badge-ring);
           display: flex; align-items: center; justify-content: center; }
  .badge span { color: var(--badge-ring); font-weight: 700; letter-spacing: 1px; }

  .title { position: absolute; font-weight: 700; text-transform: uppercase; line-height: 0.95; color: var(--white); }
  .subtitle { position: absolute; font-weight: 700; text-transform: uppercase; color: var(--orange); line-height: 1.05; }
  .offer { position: absolute; font-weight: 700; color: var(--white); line-height: 1.05; }
  .offer .pct { color: var(--orange); }

  /* Skyscraper */
  .skyscraper { left: 65px; top: 77px; width: 194px; height: 727px; }
  .skyscraper .photo { width: 194px; height: 420px; }
  .skyscraper .badge { left: 78px; top: 301px; width: 84px; height: 84px; }
  .skyscraper .badge span { font-size: 22px; }
  .skyscraper .title { left: 0; width: 194px; top: 412px; text-align: center; font-size: 50px; }
  .skyscraper .subtitle { left: 0; width: 194px; top: 530px; text-align: center; font-size: 25px; }
  .skyscraper .offer { left: 0; width: 194px; top: 610px; text-align: center; font-size: 32px; }
  .skyscraper .offer .pct { font-size: 46px; }

  /* Leaderboard */
  .leaderboard { left: 271px; top: 77px; width: 893px; height: 110px; }
  .leaderboard .photo { width: 430px; height: 110px; }
  .leaderboard .badge { left: 350px; top: 11px; width: 86px; height: 86px; }
  .leaderboard .badge span { font-size: 22px; }
  .leaderboard .title { left: 448px; top: 14px; font-size: 46px; }
  .leaderboard .subtitle { left: 450px; top: 64px; font-size: 27px; }
  .leaderboard .divider { position: absolute; left: 752px; top: 14px; width: 2px; height: 82px; background: var(--white); opacity: 0.85; }
  .leaderboard .offer { left: 768px; top: 12px; font-size: 30px; }
  .leaderboard .offer .pct { font-size: 40px; }

  /* Medium rectangle */
  .rectangle { left: 271px; top: 204px; width: 367px; height: 302px; }
  .rectangle .photo { width: 367px; height: 200px; }
  .rectangle .badge { left: 276px; top: 92px; width: 84px; height: 84px; }
  .rectangle .badge span { font-size: 22px; }
  .rectangle .title { left: 22px; top: 178px; font-size: 50px; }
  .rectangle .subtitle { left: 22px; top: 228px; font-size: 23px; }
  .rectangle .offer { left: 22px; top: 254px; font-size: 27px; }
  .rectangle .offer .pct { font-size: 36px; }
</style>
</head>
<body>

<section class="banner skyscraper" aria-label="Vortek WGT PC skyscraper banner">
  <div class="photo" role="img" aria-label="Photo of a white business jet banking through a blue sky"></div>
  <svg class="swoosh" viewBox="0 0 194 727" aria-hidden="true">
    <defs><linearGradient id="sky-blue" x1="0" y1="0" x2="0" y2="1"><stop offset="0" stop-color="#2266d0"/><stop offset="1" stop-color="#0a1f86"/></linearGradient></defs>
    <path d="M0 420 Q 90 360 194 330 L194 727 L0 727 Z" fill="url(#sky-blue)"/>
    <path d="M0 420 Q 90 360 194 330" fill="none" stroke="#f7a21b" stroke-width="7"/>
  </svg>
  <div class="badge"><span>BRQL</span></div>
  <h2 class="title">Vortek<br>WGT PC</h2>
  <p class="subtitle">Increase WGT<br>performance</p>
  <p class="offer">by <span class="pct">30%</span><br>and more!</p>
</section>

<section class="banner leaderboard" aria-label="Vortek WGT PC leaderboard banner">
  <div class="photo" role="img" aria-label="Photo of a white business jet in a blue sky"></div>
  <svg class="swoosh" viewBox="0 0 893 110" aria-hidden="true">
    <defs><linearGradient id="lb-blue" x1="0" y1="0" x2="0" y2="1"><stop offset="0" stop-color="#2266d0"/><stop offset="1" stop-color="#0a1f86"/></linearGradient></defs>
    <path d="M330 110 Q 370 40 440 0 L893 0 L893 110 Z" fill="url(#lb-blue)"/>
    <path d="M330 110 Q 370 40 440 0" fill="none" stroke="#f7a21b" stroke-width="6"/>
  </svg>
  <div class="badge"><span>BRQL</span></div>
  <h2 class="title">Vortek WGT PC</h2>
  <p class="subtitle">Increase WGT performance</p>
  <div class="divider"></div>
  <p class="offer">by <span class="pct">30%</span><br>and more!</p>
</section>

<section class="banner rectangle" aria-label="Vortek WGT PC rectangle banner">
  <div class="photo" role="img" aria-label="Photo of a white business jet banking through a blue sky"></div>
  <svg class="swoosh" viewBox="0 0 367 302" aria-hidden="true">
    <defs><linearGradient id="rc-blue" x1="0" y1="0" x2="0" y2="1"><stop offset="0" stop-color="#2266d0"/><stop offset="1" stop-color="#0a1f86"/></linearGradient></defs>
    <path d="M0 190 Q 170 160 367 100 L367 302 L0 302 Z" fill="url(#rc-blue)"/>
    <path d="M0 190 Q 170 160 367 100" fill="none" stroke="#f7a21b" stroke-width="6"/>
  </svg>
  <div class="badge"><span>BRQL</span></div>
  <h2 class="title">Vortek WGT PC</h2>
  <p class="subtitle">Increase WGT performance</p>
  <p class="offer">by <span class="pct">30%</span> and more!</p>
</section>

</body>
</html>
```